Business Card Design Project

Need a business card that stands my education platform as a whole but

Target Market(s)

Parents, families, expats in the middle east.

Industry/Entity Type

Education

Contact Information for Business Card

www.brightlane.ae
www.homesteadhub.ae
www.littlenestcarers.ae

+971552419736
helena@brightlane.ae

Font styles to use
Serif

Requirements
Must have
• Logo's and contact details

```html
<!DOCTYPE html>
<html lang="en">
<head>
<meta charset="utf-8">
<title>Bright Lane – Business Card</title>
<link href="https://fonts.googleapis.com/css2?family=Lato:wght@400;700;900&display=swap" rel="stylesheet">
<style>
  :root {
    --backdrop: #2b2b2b;
    --orange: #f08a3e;
    --orange-text: #e07a24;
    --teal: #2f7f95;
    --ink: #333333;
    --paper: #ffffff;
  }
  * { margin: 0; padding: 0; box-sizing: border-box; }
  html, body { width: 1200px; height: 873px; overflow: hidden; }
  body {
    background: var(--backdrop);
    font-family: "Lato", sans-serif;
    position: relative;
  }
  .card {
    position: absolute;
    width: 520px;
    height: 300px;
    border-radius: 18px;
    overflow: hidden;
  }
  .card--front { left: 90px; top: 130px; background: var(--orange); }
  .card--back { left: 590px; top: 440px; background: var(--paper); }

  .brand {
    position: absolute;
    display: flex;
    align-items: center;
    gap: 12px;
    font-weight: 700;
    color: var(--teal);
  }
  .brand__dot { border-radius: 50%; background: var(--teal); flex: none; }
  .card--front .brand { left: 0; right: 0; top: 124px; justify-content: center; font-size: 40px; color: var(--paper); }
  .card--front .brand__dot { width: 30px; height: 30px; background: var(--paper); }
  .card--back .brand { left: 34px; top: 56px; font-size: 28px; }
  .card--back .brand__dot { width: 22px; height: 22px; }

  .holder { position: absolute; right: 30px; top: 54px; text-align: right; }
  .holder__name { font-weight: 900; font-size: 20px; color: var(--orange-text); }
  .holder__role { font-size: 13px; color: var(--ink); margin-top: 2px; }

  .rule { position: absolute; height: 2px; background: var(--teal); }
  .rule--upper { left: 230px; right: 24px; top: 104px; }
  .rule--lower { left: 28px; width: 250px; top: 178px; }

  .sites {
    position: absolute; right: 30px; top: 122px;
    text-align: right; font-weight: 700; font-size: 13px;
    color: var(--orange-text); line-height: 1.9;
  }
  .contacts { position: absolute; left: 30px; top: 190px; list-style: none; }
  .contacts li {
    display: flex; align-items: center; gap: 12px;
    font-weight: 700; font-size: 14px; color: var(--ink);
    height: 30px;
  }
  .contacts svg { width: 16px; height: 16px; fill: var(--teal); flex: none; }
</style>
</head>
<body>
  <section class="card card--front">
    <div class="brand"><span class="brand__dot"></span>Bright Lane</div>
  </section>

  <section class="card card--back">
    <div class="brand"><span class="brand__dot"></span>Bright Lane</div>

    <div class="holder">
      <p class="holder__name">Helena Marsh</p>
      <p class="holder__role">Owner / Founder</p>
    </div>
    <div class="rule rule--upper"></div>

    <div class="sites">
      <p>www.homesteadhub.ae</p>
      <p>www.littlenestcarers.ae</p>
    </div>

    <div class="rule rule--lower"></div>
    <ul class="contacts">
      <li>
        <svg viewBox="0 0 16 16" aria-hidden="true"><path d="M3 1h3l1.5 4-2 1.3a8 8 0 0 0 4.2 4.2L11 8.5l4 1.5v3a2 2 0 0 1-2 2A12 12 0 0 1 1 3a2 2 0 0 1 2-2z"/></svg>
        +971552419736
      </li>
      <li>
        <svg viewBox="0 0 16 16" aria-hidden="true"><path d="M1 3h14v10H1z M1 3l7 6 7-6" stroke="#fff" stroke-width="1.2"/></svg>
        helena@brightlane.ae
      </li>
      <li>
        <svg viewBox="0 0 16 16" aria-hidden="true"><path d="M6.5 9.5l3-3M7 4.5l1.5-1.5a2.8 2.8 0 0 1 4 4L11 8.5M9 11.5L7.5 13a2.8 2.8 0 0 1-4-4L5 7.5" fill="none" stroke="var(--teal)" stroke-width="1.8" stroke-linecap="round"/></svg>
        www.brightlane.ae
      </li>
    </ul>
  </section>
</body>
</html>
```